Tova Brisk Fitness Coaching Project

I am a personal trainer based in London. My services include one-on-one PT sessions, bootcamps.
I would like the design to be minimalistic. With light colours: white, pink, purple.
I specialise in weight loss, flexibility, mobility.

Tova Penrick
Personal Trainer
Email: tova.penrick@mailgrove.net
tel: 07500 918 243
Instagram: Tova Brisk

Target Market(s)

adults, mostly females (age 18-50).

Industry/Entity Type

Fitness

Contact Information for Business Card

Tova Penrick
Personal Trainer
tel: 07500 918 243
Instagram: Tova Brisk

Font styles to use
Serif

Colors
eea4c8
fbd4d5
fdf9cf
cfeae6
cee9f5

Requirements
Nice to have
• minimalistic style
• easy to read and remember

```html
<!DOCTYPE html>
<html lang="en">
<head>
<meta charset="utf-8">
<title>Tova Penrick – Personal Trainer Business Card</title>
<link rel="stylesheet" href="https://fonts.googleapis.com/css2?family=Cinzel:wght@400;500&family=Cutive&display=swap">
<style>
  :root {
    --backdrop: #070809;
    --card-cream: #fbf6bf;
    --card-cream-soft: #fdf9d2;
    --card-white: #ffffff;
    --ink: #111111;
    --rule: #555555;
    --tile-light: #f4f4ee;
    --tile-shade: #e3e4d2;
  }
  * { box-sizing: border-box; margin: 0; padding: 0; }
  html, body {
    width: 757px;
    height: 1200px;
    overflow: hidden;
    background: var(--backdrop);
  }
  .stage {
    position: relative;
    width: 757px;
    height: 1200px;
    background: var(--backdrop);
  }
  .card {
    position: absolute;
    left: 0;
    width: 757px;
    overflow: hidden;
    background: linear-gradient(180deg, var(--card-cream) 0%, var(--card-white) 45%, var(--card-white) 55%, var(--card-cream-soft) 100%);
    color: var(--ink);
  }
  .card--front { top: 141px; height: 431px; }
  .card--back  { top: 684px; height: 433px; }

  .card__name {
    position: absolute;
    left: 0;
    width: 757px;
    text-align: center;
    font-family: "Cinzel", serif;
    font-weight: 500;
    line-height: 1;
    letter-spacing: 1px;
  }
  .card--front .card__name { top: 108px; font-size: 64px; }
  .card--back  .card__name { top: 94px;  font-size: 40px; }

  .card__rule {
    position: absolute;
    height: 1.5px;
    background: var(--rule);
  }
  .card--front .card__rule { top: 201px; left: 124px; width: 476px; }
  .card--back  .card__rule { top: 182px; left: 126px; width: 475px; }

  .card__role {
    position: absolute;
    top: 226px;
    left: 0;
    width: 757px;
    text-align: center;
    font-family: "Cutive", serif;
    font-size: 34px;
    line-height: 1;
  }

  .card__tiles {
    position: absolute;
    left: 558px;
    top: 236px;
    width: 199px;
    height: 197px;
    background: linear-gradient(135deg, rgba(255,255,255,0) 0%, var(--tile-light) 40%, var(--tile-shade) 70%, var(--tile-light) 100%);
    opacity: 0.85;
  }

  .contact {
    position: absolute;
    left: 0;
    width: 500px;
    height: 26px;
    display: flex;
    align-items: center;
    font-family: "Cutive", serif;
    font-size: 18px;
    line-height: 1;
  }
  .contact--email { top: 250px; }
  .contact--phone { top: 294px; }
  .contact--social { top: 335px; }
  .contact__icon {
    position: absolute;
    left: 111px;
    width: 26px;
    height: 26px;
    display: flex;
    align-items: center;
    justify-content: center;
  }
  .contact__text { position: absolute; left: 166px; }
  .contact__mark {
    width: 19px;
    height: 19px;
    background: var(--ink);
  }

  .location {
    position: absolute;
    left: 471px;
    top: 373px;
    width: 80px;
    text-align: center;
    font-family: "Cutive", serif;
    font-size: 15px;
    line-height: 1;
  }
  .location svg { display: block; margin: 0 auto 6px; }
</style>
</head>
<body>
<main class="stage">

  <section class="card card--front">
    <h1 class="card__name">Tova Penrick</h1>
    <div class="card__rule"></div>
    <p class="card__role">Personal Trainer</p>
    <div class="card__tiles" role="img" aria-label="Soft overlapping translucent square tiles decoration"></div>
  </section>

  <section class="card card--back">
    <h2 class="card__name">Tova Penrick</h2>
    <div class="card__rule"></div>

    <div class="contact contact--email">
      <span class="contact__icon">
        <svg width="26" height="20" viewBox="0 0 26 20" aria-hidden="true">
          <rect x="2" y="2" width="22" height="16" rx="1.5" fill="none" stroke="#111" stroke-width="2.4"/>
          <path d="M3 3 L13 11 L23 3" fill="none" stroke="#111" stroke-width="2.4"/>
        </svg>
      </span>
      <span class="contact__text">tova.penrick@mailgrove.net</span>
    </div>

    <div class="contact contact--phone">
      <span class="contact__icon">
        <svg width="24" height="24" viewBox="0 0 24 24" aria-hidden="true">
          <path d="M5 3 L8.5 3 L10 7.5 L7.8 9.2 C9 12 11.5 14.5 14.5 16 L16.3 13.8 L21 15.3 L21 19 C21 20.2 20 21 18.8 21 C10.5 20.5 3.5 13.5 3 5.2 C3 4 3.8 3 5 3 Z" fill="none" stroke="#111" stroke-width="2.2" stroke-linejoin="round"/>
          <path d="M14 3.5 A7 7 0 0 1 20.5 10" fill="none" stroke="#111" stroke-width="1.8"/>
          <path d="M14 7 A3.5 3.5 0 0 1 17 10" fill="none" stroke="#111" stroke-width="1.8"/>
        </svg>
      </span>
      <span class="contact__text">07500 918 243</span>
    </div>

    <div class="contact contact--social">
      <span class="contact__icon"><span class="contact__mark"></span></span>
      <span class="contact__text">Tova Brisk</span>
    </div>

    <div class="location">
      <svg width="16" height="23" viewBox="0 0 16 23" aria-hidden="true">
        <path d="M8 0 C3.6 0 0 3.5 0 7.9 C0 13.5 8 23 8 23 C8 23 16 13.5 16 7.9 C16 3.5 12.4 0 8 0 Z" fill="#222"/>
        <circle cx="8" cy="7.8" r="3" fill="#fff"/>
      </svg>
      London
    </div>

    <div class="card__tiles" role="img" aria-label="Soft overlapping translucent square tiles decoration"></div>
  </section>

</main>
</body>
</html>
```